Lantern Hill Publicity is a new boutique Press Office with a small roster of well-chosen clients across an array of disciplines; from Art and Technology to Restaurants and Fashion. Based in Greenpoint Brooklyn, Lantern Hill Publicity achieves outstanding results through hard work, tenacity, efficiency and a sense of humor. We need a simple, versatile and classic design. We would like each side of the card to be white text on a black background.

Boutique

```html
<!DOCTYPE html>
<html lang="en">
<head>
<meta charset="utf-8">
<title>Lantern Hill Publicity – Business Card</title>
<link href="https://fonts.googleapis.com/css2?family=Open+Sans:wght@400&display=swap" rel="stylesheet">
<style>
  :root {
    --stage: #3b3b3b;
    --card: #121212;
    --ink: #ffffff;
    --muted: #d9d9d9;
    --stripe: #ffffff;
  }
  html, body {
    margin: 0;
    padding: 0;
    width: 1200px;
    height: 900px;
    overflow: hidden;
    background: var(--stage);
    font-family: "Open Sans", Arial, sans-serif;
  }
  .canvas {
    position: relative;
    width: 1200px;
    height: 900px;
  }
  .card {
    position: absolute;
    left: 270px;
    width: 660px;
    height: 380px;
    background: var(--card);
    color: var(--ink);
    box-shadow: 0 12px 30px rgba(0,0,0,0.45);
    overflow: hidden;
  }
  .card::after {
    content: "";
    position: absolute;
    left: 0;
    right: 0;
    bottom: 0;
    height: 12px;
    background: var(--stripe);
  }
  .card--front { top: 40px; }
  .card--back { top: 480px; }

  .wordmark {
    font-weight: 400;
    text-transform: uppercase;
    color: var(--ink);
    letter-spacing: 0.22em;
    line-height: 1.35;
    text-align: center;
  }
  .card--front .wordmark {
    position: absolute;
    top: 118px;
    left: 0;
    right: 0;
    font-size: 30px;
  }
  .brand-dot {
    display: block;
    width: 34px;
    height: 34px;
    border-radius: 50%;
    background: var(--ink);
    margin: 0 auto 14px;
  }
  .card--front .web {
    position: absolute;
    top: 282px;
    left: 0;
    right: 0;
    text-align: center;
    font-size: 17px;
    letter-spacing: 0.08em;
  }

  .card--back .wordmark {
    position: absolute;
    top: 110px;
    left: 20px;
    width: 270px;
    font-size: 20px;
  }
  .card--back .brand-dot {
    width: 26px;
    height: 26px;
  }
  .divider {
    position: absolute;
    left: 318px;
    top: 50px;
    width: 1px;
    height: 270px;
    background: linear-gradient(to bottom, rgba(255,255,255,0), rgba(255,255,255,0.8) 50%, rgba(255,255,255,0));
  }
  .details {
    position: absolute;
    left: 350px;
    top: 50px;
    right: 20px;
  }
  .person {
    margin: 0 0 4px 40px;
    font-size: 21px;
  }
  .role, .address {
    margin: 0 0 0 40px;
    font-size: 16px;
    color: var(--muted);
    line-height: 1.4;
  }
  .address { margin-bottom: 18px; }
  .contact {
    list-style: none;
    margin: 0;
    padding: 0;
  }
  .contact li {
    display: flex;
    align-items: center;
    font-size: 17px;
    line-height: 26px;
  }
  .contact svg {
    width: 18px;
    height: 18px;
    margin-right: 22px;
    fill: var(--ink);
    flex: none;
  }
</style>
</head>
<body>
<main class="canvas">

  <section class="card card--front" aria-label="Card front">
    <div class="wordmark"><span class="brand-dot"></span>Lantern Hill<br>Publicity</div>
    <div class="web">www.lanternhillpr.com</div>
  </section>

  <section class="card card--back" aria-label="Card back">
    <div class="wordmark"><span class="brand-dot"></span>Lantern Hill<br>Publicity</div>
    <div class="divider"></div>
    <div class="details">
      <p class="person">Daniel Okafor</p>
      <p class="role">Owner &amp; Founder</p>
      <p class="address">LLC 88 Kestrel Street Unit 4<br>Brooklyn, NY 11222</p>
      <ul class="contact">
        <li>
          <svg viewBox="0 0 24 24" aria-hidden="true"><path d="M6.6 10.8a15.1 15.1 0 0 0 6.6 6.6l2.2-2.2c.3-.3.7-.4 1-.2 1.1.4 2.3.6 3.6.6.6 0 1 .4 1 1V20c0 .6-.4 1-1 1A17 17 0 0 1 3 4c0-.6.4-1 1-1h3.5c.6 0 1 .4 1 1 0 1.3.2 2.5.6 3.6.1.3 0 .7-.2 1l-2.3 2.2z"/></svg>
          917-555-0142
        </li>
        <li>
          <svg viewBox="0 0 24 24" aria-hidden="true"><path d="M7 1h10a2 2 0 0 1 2 2v18a2 2 0 0 1-2 2H7a2 2 0 0 1-2-2V3a2 2 0 0 1 2-2zm0 3v14h10V4H7zm5 15.5a1 1 0 1 0 0 2 1 1 0 0 0 0-2z"/></svg>
          917-555-0187
        </li>
        <li>
          <svg viewBox="0 0 24 24" aria-hidden="true"><path d="M2 5h20v14H2V5zm2 2v.5l8 5.5 8-5.5V7H4zm0 2.9V17h16V9.9l-8 5.5-8-5.5z"/></svg>
          daniel@lanternhillpr.com
        </li>
        <li>
          <svg viewBox="0 0 24 24" aria-hidden="true"><path d="M12 2a10 10 0 1 0 0 20 10 10 0 0 0 0-20zm6.9 6h-2.9a15 15 0 0 0-1.4-3.6A8 8 0 0 1 18.9 8zM12 4c.8 1.2 1.5 2.5 1.9 4h-3.8c.4-1.5 1.1-2.8 1.9-4zM4.3 14a8 8 0 0 1 0-4h3.4a16 16 0 0 0 0 4H4.3zm.8 2h2.9c.3 1.3.8 2.5 1.4 3.6A8 8 0 0 1 5.1 16zM8 8H5.1a8 8 0 0 1 4.3-3.6C8.8 5.5 8.3 6.7 8 8zm4 12c-.8-1.2-1.5-2.5-1.9-4h3.8c-.4 1.5-1.1 2.8-1.9 4zm2.3-6H9.7a14 14 0 0 1 0-4h4.6a14 14 0 0 1 0 4zm.3 5.6c.6-1.1 1.1-2.3 1.4-3.6h2.9a8 8 0 0 1-4.3 3.6zm1.7-5.6a16 16 0 0 0 0-4h3.4a8 8 0 0 1 0 4h-3.4z"/></svg>
          www.lanternhillpr.com
        </li>
      </ul>
    </div>
  </section>

</main>
</body>
</html>
```